Supplement Label Design - Sports Nutrition

Design a sports nutrition/weight loss supplement label that stands out in a crowded space. Supplement bottle size is 200c and label size is 7" x 2.5" approximately. We're looking for a design that emphasizes the products name called VUK. Vuk is an abbreviation for Vigor, Uplift & Keenness. We want VUK to be the center/focus point of the bottle and have a memorable design to it.

Target Market(s)

Men & Women over 18

Industry/Entity Type

Supplement

Font styles to use
Sans Serif
Decorative

Requirements
Must have
• Emphasis on the product name VUK. Serious, Inspirational & Motivational feel to the design, typo & colors. Electrocution/lightning feel to the text. Right hand side of label is our formulation. Left hand side is dedicated to explaining the trifecta formulation idea.
Nice to have
• For example, we like the graphic design of "Thud" energy drinks because you can identify the bottle from a distance and is memorable. We think that less is more and we'd like the design/colors do most of the talking.
Should not have
• Cartroon/animated style.

```html
<!DOCTYPE html>
<html lang="en">
<head>
<meta charset="utf-8">
<title>VUK – Supplement Label</title>
<link rel="stylesheet" href="https://fonts.googleapis.com/css2?family=Anton&family=Bowlby+One&family=Oswald:wght@400;700&display=swap">
<style>
  :root {
    --page-bg: #efefef;
    --label-white: #f6f6f6;
    --brand-green: #14d35e;
    --dot-green: #1fc465;
    --volt-yellow: #f2ee00;
    --ink: #111111;
    --band-dark: #161616;
    --rim-grey: #3a3a3a;
    --white: #ffffff;
  }
  * { margin: 0; padding: 0; box-sizing: border-box; }
  html, body {
    width: 1200px;
    height: 1018px;
    overflow: hidden;
    background: var(--page-bg);
  }
  .canvas {
    position: relative;
    width: 1200px;
    height: 1018px;
  }
  .label {
    position: absolute;
    left: 390px;
    top: 149px;
    width: 420px;
    height: 724px;
    background: var(--label-white);
    overflow: hidden;
    box-shadow: 0 10px 30px rgba(0,0,0,0.12);
  }
  .label__rim {
    position: absolute;
    left: 0; top: 0;
    width: 100%; height: 6px;
    background: var(--rim-grey);
  }
  .label__art {
    position: absolute;
    left: 0; top: 0;
    width: 420px; height: 724px;
  }
  .dot-field {
    position: absolute;
    left: 0;
    top: 100px;
    width: 134px;
    height: 515px;
    background: linear-gradient(180deg, rgba(31,196,101,0.10) 0%, rgba(31,196,101,0.35) 60%, rgba(31,196,101,0.55) 100%);
  }
  .potency-badge {
    position: absolute;
    left: 0;
    top: 49px;
    width: 156px;
    height: 46px;
    background: var(--volt-yellow);
    border: 2px solid var(--ink);
    border-left: none;
    clip-path: polygon(0 0, 100% 0, 86% 100%, 0 100%);
    display: flex;
    align-items: center;
    padding-left: 4px;
    font-family: "Oswald", sans-serif;
    font-size: 24px;
    letter-spacing: 0.5px;
    color: var(--ink);
    line-height: 1;
  }
  .potency-badge b { font-weight: 700; }
  .potency-badge span { font-weight: 400; }
  .product-name {
    position: absolute;
    left: 10px;
    top: 92px;
    font-family: "Anton", sans-serif;
    font-size: 200px;
    line-height: 1;
    color: var(--ink);
    letter-spacing: 2px;
  }
  .trifecta {
    position: absolute;
    left: 148px;
    top: 312px;
    font-family: "Bowlby One", sans-serif;
    font-size: 33px;
    line-height: 1.08;
    color: var(--volt-yellow);
    -webkit-text-stroke: 1.5px var(--ink);
    transform: skewX(-6deg);
    transform-origin: left top;
  }
  .trifecta span { display: block; }
  .claim {
    position: absolute;
    left: 146px;
    top: 492px;
    font-family: "Bowlby One", sans-serif;
    color: var(--ink);
    transform: skewX(-6deg);
    transform-origin: left top;
  }
  .claim__lead {
    display: block;
    font-size: 26px;
    line-height: 1.1;
  }
  .claim__energy {
    display: block;
    font-size: 46px;
    line-height: 1;
    color: var(--volt-yellow);
  }
  .claim__formula {
    display: block;
    font-size: 13px;
    line-height: 1.4;
    letter-spacing: 0.3px;
  }
  .count-band {
    position: absolute;
    left: 0;
    top: 615px;
    width: 100%;
    height: 58px;
    background: var(--band-dark);
    border-top: 4px solid var(--white);
    display: flex;
    align-items: center;
    padding-left: 4px;
    gap: 6px;
    color: var(--white);
    font-family: "Bowlby One", sans-serif;
  }
  .count-band__number {
    font-size: 36px;
    color: var(--band-dark);
    -webkit-text-stroke: 1.5px var(--white);
    line-height: 1;
  }
  .count-band__unit {
    font-size: 22px;
    line-height: 1;
    transform: skewX(-6deg);
  }
  .base-strip {
    position: absolute;
    left: 0;
    top: 673px;
    width: 100%;
    height: 51px;
    background: var(--brand-green);
  }
  .base-strip__line {
    position: absolute;
    left: 0;
    top: 10px;
    width: 100%;
    height: 4px;
    background: var(--white);
  }
</style>
</head>
<body>
<div class="canvas">
  <div class="label">
    <div class="dot-field" role="img" aria-label="Halftone pattern of green dots sweeping across the white side of the label"></div>
    <svg class="label__art" viewBox="0 0 420 724" aria-hidden="true">
      <polygon points="369,29 420,29 420,615 134,615 134,315" fill="var(--brand-green)"/>
    </svg>
    <div class="label__rim"></div>

    <div class="potency-badge"><b>HIGH</b><span>POTENCY</span></div>

    <div class="product-name">VUK</div>

    <div class="trifecta">
      <span>Vigor</span>
      <span>Uplift</span>
      <span>Keenness</span>
    </div>

    <div class="claim">
      <span class="claim__lead">Explosive</span>
      <span class="claim__energy">ENERGY</span>
      <span class="claim__formula">AND CUTTING FORMULA*</span>
    </div>

    <div class="count-band">
      <span class="count-band__number">120</span>
      <span class="count-band__unit">Capsules</span>
    </div>

    <div class="base-strip"><div class="base-strip__line"></div></div>
  </div>
</div>
</body>
</html>
```